Ruby Deck Fun Casino Entertainment

Looking to update my business card and make it look more modern, stand out and eye catching.
We are are fun casino business in Australia (primarily Sydney). Blackjack and Roulette are our most popular games although we have pretty much every game available for hire that you would find in a real casino. The final design would need to be sleek and appeal to the more upmarket corporate sector.
We mainly cater for Corporate Events, Private Parties, Fundraising Events, Team Building, Poker Tournaments
I think I'd prefer the colour Black.

Target Market(s)

High-end Corporate

Industry/Entity Type

Events

Contact Information for Business Card

Ned Paxley
Director
1300 472 861
0438 705 705
info@rubydeckfun.com.au
www.rubydeckfun.com.au
Facebook & Instagram @rubydeckshowhire (proper social icons preferred)

Colors
000000
0255a3

Requirements
Must have
• Front side:
• Logo
• Contact details
• 'Australia's #1 Fun Casino Specialists'
• Back:
• Logo
Nice to have
• Back:
• Corporate Events
• Private Parties
• Poker Tournaments
• Fundraising
• Props & Theming
• Photo Booth
• Horse Racing Events
• The Vegas Sign attached, maybe on the back of the card in the background...?

```html
<!DOCTYPE html>
<html lang="en">
<head>
<meta charset="utf-8">
<title>Ruby Deck Fun Casino Entertainment – Business Card</title>
<link rel="stylesheet" href="https://fonts.googleapis.com/css2?family=Exo+2:wght@400;500;700;800&display=swap">
<style>
  :root {
    --stage: #2b2d31;
    --card: #050505;
    --card-edge: #1a1a1a;
    --gold: #ffb000;
    --gold-light: #ffd21a;
    --orange: #ff9a00;
    --text: #e9e9e9;
    --muted: #bdbdbd;
  }
  * { box-sizing: border-box; margin: 0; padding: 0; }
  html, body {
    width: 1200px; height: 900px; overflow: hidden;
    background: var(--stage);
    font-family: "Exo 2", sans-serif;
  }
  .sheet {
    position: relative; width: 1200px; height: 900px;
    display: flex; align-items: center; justify-content: center; gap: 40px;
  }
  .card {
    position: relative; width: 540px; height: 330px;
    background: radial-gradient(ellipse at 40% 30%, #1b1b1b, var(--card) 70%);
    border-radius: 26px; overflow: hidden;
    border: 1px solid var(--card-edge);
  }

  /* brand name block */
  .brand {
    position: absolute; display: flex; align-items: center; gap: 12px;
  }
  .brand-dot {
    width: 46px; height: 46px; border-radius: 50%;
    background: var(--gold); flex: none;
  }
  .brand-name {
    font-weight: 800; font-size: 38px; letter-spacing: 1px;
    color: var(--gold); text-transform: uppercase; line-height: 1;
    white-space: nowrap;
  }

  /* front */
  .front .brand { left: 30px; top: 84px; gap: 10px; }
  .front .brand-dot { width: 38px; height: 38px; }
  .front .brand-name { font-size: 29px; letter-spacing: 0.5px; }
  .contact { position: absolute; left: 304px; top: 58px; width: 214px; }
  .person-name {
    font-weight: 800; font-size: 26px; color: var(--gold);
    letter-spacing: 1px; text-transform: uppercase; line-height: 1;
  }
  .person-role {
    font-weight: 700; font-size: 13px; color: #fff;
    letter-spacing: 1px; margin-top: 4px;
  }
  .rule { height: 1.5px; background: var(--gold); margin: 10px 0; }
  .social { display: flex; align-items: center; gap: 6px; font-size: 12.5px; color: var(--text); }
  .social-dot { width: 16px; height: 16px; border-radius: 50%; background: #3b5bb5; flex: none; }
  .social-dot.second { background: #d43aa5; }
  .details { list-style: none; margin-top: 2px; }
  .details li {
    display: flex; align-items: center; gap: 8px;
    font-size: 13.5px; color: var(--text); line-height: 1.45;
    white-space: nowrap;
  }
  .details svg { width: 12px; height: 12px; flex: none; fill: var(--gold); }
  .tagline-band {
    position: absolute; left: 0; right: 0; bottom: 0; height: 56px;
    background: linear-gradient(90deg, var(--orange), var(--gold-light));
    display: flex; align-items: center; padding-left: 34px;
  }
  .tagline { font-weight: 700; font-size: 17px; color: #111; }

  /* back */
  .back .brand { left: 40px; top: 110px; }
  .services {
    position: absolute; left: 330px; top: 60px; list-style: none;
  }
  .services li {
    display: flex; align-items: center; gap: 9px;
    font-size: 15px; font-weight: 500; color: var(--text);
    line-height: 1.95; white-space: nowrap;
  }
  .services svg { width: 10px; height: 10px; fill: var(--gold); flex: none; }
</style>
</head>
<body>
<main class="sheet">

  <section class="card front" aria-label="Business card front">
    <div class="brand">
      <span class="brand-dot"></span>
      <span class="brand-name">Ruby Deck</span>
    </div>

    <div class="contact">
      <h1 class="person-name">Ned Paxley</h1>
      <p class="person-role">DIRECTOR</p>
      <div class="rule"></div>
      <div class="social">
        <span class="social-dot"></span>
        <span class="social-dot second"></span>
        <span>@rubydeckshowhire</span>
      </div>
      <div class="rule"></div>
      <ul class="details">
        <li><svg viewBox="0 0 12 12"><path d="M2.5 1l2 2.2-1 1.3c.7 1.5 1.8 2.6 3.3 3.3l1.3-1 2.2 2-1.1 1.7C5 10 2 7 .8 2.1z"/></svg>1300 472 861</li>
        <li><svg viewBox="0 0 12 12"><path d="M3 0h6a1 1 0 0 1 1 1v10a1 1 0 0 1-1 1H3a1 1 0 0 1-1-1V1a1 1 0 0 1 1-1zm.5 1.5v8h5v-8z"/></svg>0438 705 705</li>
        <li><svg viewBox="0 0 12 12"><path d="M0 2h12v8H0zm1 1l5 3.5L11 3z"/></svg>info@rubydeckfun.com.au</li>
        <li><svg viewBox="0 0 12 12"><path d="M6 0a6 6 0 1 0 0 12A6 6 0 0 0 6 0zm0 1.2a4.8 4.8 0 1 1 0 9.6 4.8 4.8 0 0 1 0-9.6zM1.5 5.5h9v1h-9zM5.5 1.5h1v9h-1z"/></svg>www.rubydeckfun.com.au</li>
      </ul>
    </div>

    <div class="tagline-band">
      <p class="tagline">Australia's #1 Fun Casino Specialists</p>
    </div>
  </section>

  <section class="card back" aria-label="Business card back">
    <div class="brand">
      <span class="brand-dot"></span>
      <span class="brand-name">Ruby Deck</span>
    </div>

    <ul class="services">
      <li><svg viewBox="0 0 10 10"><path d="M5 0l5 5-5 5-5-5z"/></svg>Corporate Events</li>
      <li><svg viewBox="0 0 10 10"><path d="M5 0l5 5-5 5-5-5z"/></svg>Private Parties</li>
      <li><svg viewBox="0 0 10 10"><path d="M5 0l5 5-5 5-5-5z"/></svg>Poker Tournaments</li>
      <li><svg viewBox="0 0 10 10"><path d="M5 0l5 5-5 5-5-5z"/></svg>Fundraising</li>
      <li><svg viewBox="0 0 10 10"><path d="M5 0l5 5-5 5-5-5z"/></svg>Props &amp; Theming</li>
      <li><svg viewBox="0 0 10 10"><path d="M5 0l5 5-5 5-5-5z"/></svg>Photo Booth</li>
      <li><svg viewBox="0 0 10 10"><path d="M5 0l5 5-5 5-5-5z"/></svg>Horse Racing Events</li>
    </ul>
  </section>

</main>
</body>
</html>
```